Professional Baby Bottle Bank Print Design

We need a baby bottle design that is 4.25" wide x 2.28" tall with a maximum of 6 colors (white is counted as a color).

The bottle design needs to be fun but professional. Bottles with cartoon images on it will be rejected immediately.

The bottle design wraps around the bottle. See examples here: https://wendrix.net/cat/BabyBottles/OrvelJarsKit/5

Minimum font size is 10pt.

The bottle design must have the following text on it:
Main Text: Love them both
Paragraph text: Our ministry’s aim is to not only save unborn babies, but to provide love, support, and life-saving resources for vulnerable women in our community. By filling this bottle with cash, checks, and spare coins and returning it on collection day, you are truly saving and changing lives!
Optional text: Thank you!

We are including an example file and a template file. You do NOT have to use the template - but your file has to be the exact size mentioned. If you don't design as well as our sample, please don't waste our time by spamming us with hundreds of designs. We will ban design houses that spam us with designs that are more layouts (and not well designed).

Please note - white is a color. You don't have to do a box - but anything you don't make white will be see-through.

We will take the winners of this contest to a survey with the customers. We may choose two and edit the text of one slightly to be different. We must know the fonts used.

No gradients unless they are half-toned with relatively big sized dots.

Target Market(s)

Church Attendees coming from a Pregnancy Center

Industry/Entity Type

Religious Christian Churches

Requirements
Must have
• Professional, great palette, wording as described.
Nice to have
• Integrated design across the whole space with areas for text (no text all the way across)
Should not have
• Cartoon figures; elements shoved together that don't go together (i.e. - actually design something)

```html
<!DOCTYPE html>
<html lang="en">
<head>
<meta charset="utf-8">
<title>Love Them Both – Baby Bottle Wrap</title>
<link rel="stylesheet" href="https://fonts.googleapis.com/css2?family=Fraunces:opsz,wght,SOFT@9..144,700,100&family=Montserrat:wght@400&family=Mr+Dafoe&display=swap">
<style>
  :root {
    --peach: #f9c6ae;
    --blush: #f7cfd8;
    --pink-soft: #f5d6e4;
    --lavender: #dcd3ef;
    --ice: #e3e6f6;
    --coral: #f08f8f;
    --ink: #1f1f22;
  }
  * { margin: 0; padding: 0; box-sizing: border-box; }
  html, body { width: 1200px; height: 644px; overflow: hidden; }
  .bottle-wrap {
    position: relative;
    width: 1200px;
    height: 644px;
    overflow: hidden;
    background:
      radial-gradient(ellipse 520px 360px at 520px 80px, rgba(249,190,160,0.9), transparent 70%),
      radial-gradient(ellipse 420px 300px at 1100px 40px, rgba(247,200,214,0.9), transparent 70%),
      radial-gradient(ellipse 520px 320px at 80px 560px, rgba(214,216,242,0.95), transparent 70%),
      radial-gradient(ellipse 640px 260px at 700px 640px, rgba(226,214,240,0.9), transparent 70%),
      linear-gradient(135deg, var(--blush) 0%, var(--peach) 40%, var(--pink-soft) 70%, var(--lavender) 100%);
  }
  .flow-line {
    position: absolute;
    inset: 0;
    width: 1200px;
    height: 644px;
  }
  .flow-line path {
    fill: none;
    stroke: var(--coral);
    stroke-width: 3;
    stroke-linecap: round;
  }
  .headline {
    position: absolute;
    left: 70px;
    top: 62px;
    font-family: "Fraunces", Georgia, serif;
    font-weight: 700;
    font-variation-settings: "SOFT" 100, "opsz" 144;
    font-size: 112px;
    line-height: 88px;
    letter-spacing: -3px;
    color: var(--coral);
  }
  .headline span { display: block; }
  .headline .line-them { padding-left: 82px; }
  .headline .line-both { padding-left: 52px; }
  .mother-child-art {
    position: absolute;
    left: 445px;
    top: 130px;
    width: 255px;
    height: 315px;
    border-radius: 48% 52% 40% 60% / 45% 40% 60% 55%;
    background: radial-gradient(ellipse at 50% 45%, rgba(240,143,143,0.18), rgba(240,143,143,0.04) 70%);
  }
  .mission {
    position: absolute;
    right: 71px;
    top: 88px;
    width: 420px;
    text-align: right;
    font-family: "Montserrat", Arial, sans-serif;
    font-size: 21px;
    line-height: 28.4px;
    color: var(--ink);
  }
  .thanks {
    position: absolute;
    left: 845px;
    top: 418px;
    font-family: "Mr Dafoe", cursive;
    font-size: 78px;
    line-height: 1;
    color: var(--ink);
  }
</style>
</head>
<body>
<main class="bottle-wrap">
  <svg class="flow-line" viewBox="0 0 1200 644" aria-hidden="true">
    <path d="M0 588 C120 575 260 565 360 555 C420 548 450 520 448 470 C446 440 452 425 470 410"/>
    <path d="M690 420 C720 440 735 470 745 520 C755 565 775 575 820 570 C900 560 1000 555 1200 560"/>
  </svg>

  <h1 class="headline">
    <span class="line-love">love</span>
    <span class="line-them">them</span>
    <span class="line-both">both</span>
  </h1>

  <div class="mother-child-art" role="img" aria-label="Single-line drawing of a mother and her baby in profile, facing each other"></div>

  <p class="mission">
    Our ministry’s aim is to not<br>
    only save unborn babies,<br>
    but to provide love, support,<br>
    and life-saving resources for<br>
    vulnerable women in our<br>
    community. By filling this<br>
    bottle with cash, checks,<br>
    and spare coins and<br>
    returning it on collection<br>
    day, you are truly saving<br>
    and changing lives!
  </p>

  <p class="thanks">Thank you!</p>
</main>
</body>
</html>
```